Healthcare/Medical Consultant Company

KTL is a Healthcare Conultant Company. We help doctors manage the business side of their medical practice.
We already have a very basic world press design. We want an upgraded design that conveys partnership, healthcare expertise and healthcare innovation to our client. It needs to have a sleek, clean, modern and inclusive look. Pictures need need to convey diversity (including pictures of people of all races and shows both men and women working together in a healthcare environment to make it better). The Pictures on the home page should particularly illustrate diversity and Healthcare expertise. The company logo is blue and white but the site doesn’t have to follow the exact same theme but the logo needs to blend well with the chosen theme. The logo should ideally be in the header of the website. We would also like the following included in our website:

1. Pages should include: a home page, About Us page, Services page, Get a quote page, Contact Us page, Staff page(where we can add pictures and bio for staff).

2. The Drop down menu for services should have hyperlinks ( for each service)Leading to a page that provides detailed info about that specific service. Our services include: Revenue Cycle Management, Regulatory Compliance, Human Resources Management, & practice Management.

3. Links to social media should in the header or footer of each page.

4. Contact info should be in the footer of each page.

5. Clients should be an email to us from the contact page.

Target Market(s)

Physician Medical Practices

Industry/Entity Type

Medical

Coding

Coded - Design and coding required

Font styles to use
Sans Serif

Colors

Designer to choose colors to be used in the design.

Requirements
Must have
• See project description
Nice to have
• See project description

```html
<!DOCTYPE html>
<html lang="en">
<head>
<meta charset="utf-8">
<title>KTL – Kestrel Total Lifecare</title>
<link href="https://fonts.googleapis.com/css2?family=Lato:wght@400;700;900&family=Roboto:wght@400;500;700&display=swap" rel="stylesheet">
<style>
:root{
  --blue:#0a55a8;
  --blue-dark:#063f82;
  --sky:#2a9fd8;
  --ink:#1d2b3a;
  --text:#4a4f55;
  --muted:#8a9098;
  --line:#dfe3e8;
  --dark:#1a2230;
  --white:#ffffff;
}
*{box-sizing:border-box;margin:0;padding:0}
html,body{width:1200px;height:3600px;overflow:hidden}
body{position:relative;font-family:"Lato",sans-serif;color:var(--text);background:var(--white)}
.abs{position:absolute}
a{color:inherit;text-decoration:none}

/* top bar */
.topbar{left:0;top:0;width:1200px;height:41px;background:linear-gradient(90deg,var(--blue-dark),var(--sky));color:#fff;font-size:16px}
.topbar .social{left:74px;top:10px;display:flex;gap:24px;font-weight:700}
.topbar .contact{right:94px;top:10px;display:flex;gap:60px}
.topbar .contact span{display:flex;align-items:center;gap:12px}

/* header */
.header{left:0;top:41px;width:1200px;height:105px;background:#fff}
.brand{left:64px;top:20px;display:flex;align-items:center;gap:12px}
.brand-mark{width:16px;height:16px;border-radius:50%;background:var(--blue)}
.brand-name{font-family:"Lato",sans-serif;font-weight:700;color:var(--blue);font-size:30px;line-height:1}
.brand-sub{font-family:"Lato",sans-serif;font-weight:700;color:var(--blue);font-size:13px;margin-top:4px}
.nav{left:480px;top:42px;display:flex;gap:58px;font-family:"Roboto",sans-serif;font-size:16px;color:#555}
.nav .active{color:var(--blue);font-weight:700;position:relative}
.nav .active::after{content:"";position:absolute;left:12px;top:28px;width:16px;height:4px;background:var(--blue);border-radius:2px}
.search{left:1085px;top:36px;width:38px;height:38px;border-radius:50%;background:#eef2f7;display:flex;align-items:center;justify-content:center}

/* hero */
.hero{left:0;top:146px;width:1200px;height:580px;overflow:hidden}
.hero-photo{position:absolute;inset:0;background:linear-gradient(90deg,#0c1624 0%,#3a4655 32%,#c9d3dc 60%,#eef1f4 100%)}
.hero-title{left:79px;top:176px;color:#fff;font-weight:900;font-size:27px;line-height:38px;letter-spacing:.5px}
.hero-sub{left:79px;top:272px;color:#fff;font-weight:700;font-size:16px}
.btn{display:inline-flex;align-items:center;justify-content:center;background:var(--blue);color:#fff;font-family:"Roboto",sans-serif;font-weight:700;font-size:13px;border-radius:22px;letter-spacing:.5px}
.hero .btn{position:absolute;left:79px;top:324px;width:133px;height:42px}

/* welcome */
.section-title{font-family:"Lato",sans-serif;font-weight:900;font-size:27px;color:var(--ink)}
.section-title .accent{color:var(--sky)}
.welcome-title{left:79px;top:778px;color:var(--blue)}
.welcome-title .accent{color:var(--sky)}
.welcome-copy{left:79px;top:842px;width:530px;font-size:15px;line-height:26px;color:var(--text)}
.welcome-copy p+p{margin-top:20px}
.welcome .btn{position:absolute;left:77px;top:1052px;width:136px;height:42px}
.photo-team{left:780px;top:782px;width:343px;height:221px;background:linear-gradient(135deg,#dfe8f0,#8fa6bc)}
.photo-consult{left:670px;top:936px;width:218px;height:158px;background:linear-gradient(135deg,#cfd9e3,#7c8fa4);border:6px solid #fff}
.play{left:740px;top:901px;width:80px;height:80px;border-radius:50%;background:rgba(255,255,255,.75);display:flex;align-items:center;justify-content:center}
.play span{width:48px;height:48px;border-radius:50%;background:#fff;border:3px solid var(--blue);display:flex;align-items:center;justify-content:center}

/* services */
.services{left:0;top:1140px;width:1200px;height:620px;overflow:hidden}
.services-photo{position:absolute;inset:0;background:linear-gradient(120deg,#2a3544,#4b5868 50%,#2c3745)}
.services-title{left:0;width:1200px;top:1258px;text-align:center;color:#fff}
.lead{width:1200px;left:0;text-align:center;font-size:15px;line-height:28px;color:#fff}
.services .lead{top:1318px}
.svc-label{font-family:"Roboto",sans-serif;font-weight:500;font-size:15px;color:var(--sky);white-space:nowrap}
.svc-icon{width:62px;height:62px;border-radius:50%;background:#fff;display:flex;align-items:center;justify-content:center}
.hub{left:550px;top:1605px;width:100px;height:100px;border-radius:50%;background:#d9dde2;display:flex;justify-content:center;padding-top:28px;font-weight:700;color:#fff;font-size:26px}

/* team */
.team-title{left:0;width:1200px;top:1812px;text-align:center}
.card{top:1877px;width:235px;height:302px;border:1px solid var(--line);background:#fff;overflow:hidden}
.card-photo{position:absolute;left:0;top:0;width:235px;height:208px;background:linear-gradient(180deg,#e6e9ec,#3c4148)}
.card-social{position:absolute;top:166px;width:100%;display:flex;justify-content:center;gap:22px;color:#fff;font-size:13px;font-weight:700}
.card-name{position:absolute;top:228px;width:100%;text-align:center;color:var(--sky);font-weight:700;font-size:16px}
.card-role{position:absolute;top:256px;width:100%;text-align:center;color:var(--muted);font-size:14px}

/* contact */
.contact{left:0;top:2232px;width:1200px;height:690px;overflow:hidden}
.contact-photo{position:absolute;inset:0;background:linear-gradient(120deg,#39424e,#5a6470 45%,#2a323d)}
.contact-title{left:0;width:1200px;top:2354px;text-align:center;color:#fff}
.contact .lead{top:2414px}
.field{left:408px;width:384px;height:41px;border:1px solid rgba(255,255,255,.55);color:rgba(255,255,255,.7);font-size:14px;padding:10px 12px}
.field.focus{border-color:#fff;color:#fff}
.field.msg{height:72px}
.contact .btn{position:absolute;left:408px;top:2748px;width:138px;height:38px}

/* subscribe */
.subscribe-title{left:0;width:1200px;top:2978px;text-align:center;color:var(--blue)}
.subscribe-title .accent{color:var(--sky)}
.subscribe-copy{left:0;width:1200px;top:3045px;text-align:center;font-size:15px;color:var(--text)}
.subscribe-input{left:420px;top:3100px;width:360px;height:42px;border-bottom:1px solid var(--line);display:flex;align-items:center;justify-content:space-between;padding:0 10px;font-size:14px;color:var(--text)}

/* footer */
.footer{left:0;top:3204px;width:1200px;height:396px;overflow:hidden}
.footer-photo{position:absolute;inset:0;background:linear-gradient(120deg,#1a2230,#2d3848 55%,#1c2430)}
.f-col h4{font-family:"Roboto",sans-serif;font-weight:700;color:var(--sky);font-size:15px;margin-bottom:18px}
.f-col li{list-style:none;color:#fff;font-size:14px;line-height:31px}
.f-contact{display:flex;gap:16px;color:#fff;font-size:14px;line-height:22px;margin-bottom:24px}
.f-brand{left:900px;top:3316px;width:240px;text-align:center;color:#fff}
.f-brand .brand-name{color:#fff;font-size:28px}
.f-brand .brand-sub{color:#fff}
.f-brand p{font-size:15px;line-height:24px;margin-top:18px}
.f-rule{left:79px;top:3533px;width:1042px;height:1px;background:rgba(255,255,255,.3)}
.copyright{left:79px;top:3558px;color:#fff;font-size:14px;font-weight:700}
.f-social{left:1000px;top:3546px;display:flex;gap:12px}
.f-social span{width:34px;height:34px;border-radius:50%;border:1px solid #fff;background:#fff;color:var(--dark);font-size:13px;font-weight:700;display:flex;align-items:center;justify-content:center}
</style>
</head>
<body>

<!-- top bar -->
<div class="abs topbar">
  <div class="abs social"><span>f</span><span>t</span><span>in</span></div>
  <div class="abs contact">
    <span><svg width="18" height="14" viewBox="0 0 18 14"><rect x="1" y="1" width="16" height="12" rx="1" fill="none" stroke="#fff" stroke-width="1.6"/><path d="M1 2l8 6 8-6" fill="none" stroke="#fff" stroke-width="1.6"/></svg>support@ktl-health.example</span>
    <span><svg width="16" height="16" viewBox="0 0 16 16"><path d="M3 1l3 3-2 2c1 2 3 4 5 5l2-2 3 3-2 3C6 14 2 10 1 3z" fill="#fff"/></svg>(555) 014-0199</span>
  </div>
</div>

<!-- header -->
<header class="abs header">
  <div class="abs brand">
    <div class="brand-mark"></div>
    <div><div class="brand-name">KTL</div><div class="brand-sub">Kestrel Total Lifecare LLC</div></div>
  </div>
  <nav class="abs nav">
    <a class="active">Home</a><a>About Us</a><a>Services</a><a>Get A Quote</a><a>Contact Us</a>
  </nav>
  <div class="abs search"><svg width="18" height="18" viewBox="0 0 18 18"><circle cx="7.5" cy="7.5" r="5.5" fill="none" stroke="#0a55a8" stroke-width="2"/><path d="M12 12l4.5 4.5" stroke="#0a55a8" stroke-width="2.4" stroke-linecap="round"/></svg></div>
</header>

<!-- hero -->
<section class="abs hero">
  <div class="hero-photo" role="img" aria-label="Diverse healthcare professionals meeting around a table in a bright office"></div>
  <h1 class="abs hero-title">KESTREL TOTAL LIFECARE<br>SOLUTIONS LLC</h1>
  <p class="abs hero-sub">Advancing Health Care</p>
  <a class="btn">GET A QUOTE</a>
  <svg class="abs" style="left:0;top:470px" width="1200" height="110" viewBox="0 0 1200 110">
    <path d="M0 110 L0 100 Q600 -20 1200 100 L1200 110 Z" fill="#fff"/>
    <path d="M0 100 Q600 -20 1200 92" fill="none" stroke="#0a55a8" stroke-width="6"/>
  </svg>
</section>

<!-- welcome -->
<section class="welcome">
  <h2 class="abs section-title welcome-title"><span class="accent">Welcome To</span> Kestrel Total Lifecare</h2>
  <div class="abs welcome-copy">
    <p>Lorem Ipsum is simply dummy text of the printing and typesetting industry. Lorem Ipsum has been the industry's standard dummy text ever since the 1500s, when an unknown printer took a galley of type and scrambled it to make a type specimen book.</p>
    <p>It has survived not only five centuries, but also the leap into electronic typesetting, remaining essentially unchanged.</p>
  </div>
  <a class="btn">LEARN MORE</a>
  <div class="abs photo-team" role="img" aria-label="Medical team reviewing records together at a meeting table"></div>
  <div class="abs photo-consult" role="img" aria-label="Doctor consulting with a colleague"></div>
  <div class="abs play"><span><svg width="16" height="18" viewBox="0 0 16 18"><path d="M3 2l11 7-11 7z" fill="#0a55a8"/></svg></span></div>
</section>

<!-- services -->
<section class="abs services">
  <div class="services-photo" role="img" aria-label="Healthcare staff working together, darkened background"></div>
</section>
<svg class="abs" style="left:0;top:1130px" width="1200" height="90" viewBox="0 0 1200 90"><path d="M0 0 H1200 V40 Q600 150 0 40 Z" fill="#fff"/></svg>
<h2 class="abs section-title services-title"><span class="accent">Our</span> Services</h2>
<p class="abs lead" style="top:1318px">Lorem Ipsum is simply dummy text of the printing and typesetting industry. Lorem Ipsum<br>has been the industry's standard dummy text ever since the 1500s</p>
<svg class="abs" style="left:300px;top:1380px" width="600" height="360" viewBox="0 0 600 360">
  <g fill="none" stroke="rgba(255,255,255,.35)" stroke-width="1.5">
    <circle cx="300" cy="276" r="175"/>
    <circle cx="300" cy="276" r="120"/>
    <circle cx="300" cy="276" r="80"/>
  </g>
</svg>
<div class="abs hub">KTL</div>
<div class="abs svc-icon" style="left:569px;top:1450px"><svg width="30" height="30" viewBox="0 0 30 30"><rect x="5" y="4" width="16" height="22" rx="2" fill="none" stroke="#0a55a8" stroke-width="2"/><path d="M9 10h8M9 15h8M9 20h5" stroke="#0a55a8" stroke-width="2"/><path d="M19 22l3 3 6-8" fill="none" stroke="#2a9fd8" stroke-width="2.4"/></svg></div>
<div class="abs svc-label" style="left:506px;top:1405px">Regulatory Compliance</div>
<div class="abs svc-icon" style="left:444px;top:1493px"><svg width="30" height="30" viewBox="0 0 30 30"><rect x="7" y="3" width="16" height="24" rx="2" fill="none" stroke="#0a55a8" stroke-width="2"/><path d="M11 10h8M11 15h8M11 20h8" stroke="#0a55a8" stroke-width="2"/></svg></div>
<div class="abs svc-label" style="left:226px;top:1513px">Medical Billing &amp; Coding</div>
<div class="abs svc-icon" style="left:691px;top:1493px"><svg width="32" height="30" viewBox="0 0 32 30"><circle cx="16" cy="10" r="5" fill="#0a55a8"/><circle cx="6" cy="13" r="4" fill="#0a55a8"/><circle cx="26" cy="13" r="4" fill="#0a55a8"/><path d="M6 26a10 10 0 0 1 20 0z" fill="#0a55a8"/></svg></div>
<div class="abs svc-label" style="left:776px;top:1513px">Human Resources Training</div>
<div class="abs svc-icon" style="left:389px;top:1596px"><svg width="30" height="30" viewBox="0 0 30 30"><path d="M24 11a10 10 0 0 0-18-2M6 19a10 10 0 0 0 18 2" fill="none" stroke="#0a55a8" stroke-width="2.2"/><path d="M4 5v5h5M26 25v-5h-5" fill="none" stroke="#0a55a8" stroke-width="2.2"/><text x="15" y="19" text-anchor="middle" font-family="Roboto,sans-serif" font-size="11" font-weight="700" fill="#2a9fd8">$</text></svg></div>
<div class="abs svc-label" style="left:132px;top:1617px">Revenue Cycle Management</div>
<div class="abs svc-icon" style="left:749px;top:1596px"><svg width="30" height="30" viewBox="0 0 30 30"><rect x="4" y="4" width="22" height="16" rx="1" fill="none" stroke="#0a55a8" stroke-width="2"/><path d="M8 16l5-5 4 3 5-5" fill="none" stroke="#2a9fd8" stroke-width="2"/><path d="M15 20v6M10 27h10" stroke="#0a55a8" stroke-width="2"/></svg></div>
<div class="abs svc-label" style="left:834px;top:1617px">Staff Education and Training</div>
<svg class="abs" style="left:0;top:1660px" width="1200" height="110" viewBox="0 0 1200 110"><path d="M0 100 Q600 -30 1200 40 V110 H0 Z" fill="#fff"/></svg>

<!-- team -->
<h2 class="abs section-title team-title"><span class="accent">Our</span> Team</h2>
<article class="abs card" style="left:77px">
  <div class="card-photo" role="img" aria-label="Team member portrait"></div>
  <svg class="abs" style="left:0;top:168px" width="235" height="42" viewBox="0 0 235 42"><path d="M0 42 V28 Q117 -10 235 28 V42 Z" fill="#fff"/></svg>
  <div class="card-social" style="top:136px"><span>f</span><span>t</span><span>in</span></div>
  <div class="card-name">Member Name</div><div class="card-role">Position</div>
</article>
<article class="abs card" style="left:348px">
  <div class="card-photo" role="img" aria-label="Team member portrait"></div>
  <svg class="abs" style="left:0;top:168px" width="235" height="42" viewBox="0 0 235 42"><path d="M0 42 V28 Q117 -10 235 28 V42 Z" fill="#fff"/></svg>
  <div class="card-social" style="top:136px"><span>f</span><span>t</span><span>in</span></div>
  <div class="card-name">Member Name</div><div class="card-role">Position</div>
</article>
<article class="abs card" style="left:617px">
  <div class="card-photo" role="img" aria-label="Team member portrait"></div>
  <svg class="abs" style="left:0;top:168px" width="235" height="42" viewBox="0 0 235 42"><path d="M0 42 V28 Q117 -10 235 28 V42 Z" fill="#fff"/></svg>
  <div class="card-social" style="top:136px"><span>f</span><span>t</span><span>in</span></div>
  <div class="card-name">Member Name</div><div class="card-role">Position</div>
</article>
<article class="abs card" style="left:888px">
  <div class="card-photo" role="img" aria-label="Team member portrait"></div>
  <svg class="abs" style="left:0;top:168px" width="235" height="42" viewBox="0 0 235 42"><path d="M0 42 V28 Q117 -10 235 28 V42 Z" fill="#fff"/></svg>
  <div class="card-social" style="top:136px"><span>f</span><span>t</span><span>in</span></div>
  <div class="card-name">Member Name</div><div class="card-role">Position</div>
</article>

<!-- contact -->
<section class="abs contact">
  <div class="contact-photo" role="img" aria-label="Colleagues talking in a modern office, darkened background"></div>
</section>
<svg class="abs" style="left:0;top:2225px" width="1200" height="100" viewBox="0 0 1200 100"><path d="M0 0 H1200 V20 Q600 120 0 20 Z" fill="#fff"/></svg>
<h2 class="abs section-title contact-title"><span class="accent">Contact</span> Us</h2>
<p class="abs lead" style="top:2414px">Lorem Ipsum is simply dummy text of the printing and typesetting industry. Lorem Ipsum<br>has been the industry's standard dummy text ever since the 1500s</p>
<div class="abs field focus" style="top:2503px">Name*</div>
<div class="abs field" style="top:2554px">E-mail*</div>
<div class="abs field" style="top:2606px">Phone*</div>
<div class="abs field msg" style="top:2659px">Message</div>
<a class="abs btn" style="left:408px;top:2748px;width:138px;height:38px">SUBMIT NOW!</a>
<svg class="abs" style="left:0;top:2820px" width="1200" height="110" viewBox="0 0 1200 110"><path d="M0 100 Q600 -40 1200 100 V110 H0 Z" fill="#fff"/></svg>

<!-- subscribe -->
<h2 class="abs section-title subscribe-title">Subscribe <span class="accent">Us!</span></h2>
<p class="abs subscribe-copy">For latest news or updates subscribe our newsletter</p>
<div class="abs subscribe-input"><span>Enter e-mail*</span><svg width="20" height="18" viewBox="0 0 20 18"><path d="M1 8L19 1 14 17 10 11z" fill="#0a55a8"/></svg></div>

<!-- footer -->
<footer class="abs footer">
  <div class="footer-photo" role="img" aria-label="Office team at work, darkened background"></div>
</footer>
<svg class="abs" style="left:0;top:3200px" width="1200" height="80" viewBox="0 0 1200 80"><path d="M0 0 H1200 V50 Q600 -10 0 30 Z" fill="#fff"/><path d="M0 30 Q600 -10 1200 50" fill="none" stroke="#0a55a8" stroke-width="6"/></svg>
<div class="abs f-col" style="left:79px;top:3318px"><h4>Navigation</h4><ul><li>Home</li><li>About Us</li><li>Services</li><li>Get A Quote</li><li>Contact Us</li></ul></div>
<div class="abs f-col" style="left:348px;top:3318px">
  <h4>Get In Touch</h4>
  <div class="f-contact"><svg width="16" height="22" viewBox="0 0 16 22"><path d="M8 1a7 7 0 0 1 7 7c0 5-7 13-7 13S1 13 1 8a7 7 0 0 1 7-7z" fill="none" stroke="#2a9fd8" stroke-width="2"/><circle cx="8" cy="8" r="2.5" fill="#2a9fd8"/></svg><span>180 Harbor Lane<br>Springfield, ST 00100</span></div>
  <div class="f-contact"><svg width="16" height="16" viewBox="0 0 16 16"><path d="M3 1l3 3-2 2c1 2 3 4 5 5l2-2 3 3-2 3C6 14 2 10 1 3z" fill="#2a9fd8"/></svg><span>(555) 014-0199</span></div>
  <div class="f-contact"><svg width="18" height="14" viewBox="0 0 18 14"><rect x="1" y="1" width="16" height="12" rx="1" fill="none" stroke="#2a9fd8" stroke-width="1.6"/><path d="M1 2l8 6 8-6" fill="none" stroke="#2a9fd8" stroke-width="1.6"/></svg><span>support@ktl-health.example</span></div>
</div>
<div class="abs f-col" style="left:619px;top:3318px"><h4>Services</h4><ul><li>Revenue Cycle Management</li><li>Medical Billing &amp; Coding</li><li>Regulatory Compliance</li><li>Human Resources Training</li><li>Staff Education and Training</li></ul></div>
<div class="abs f-brand">
  <div class="brand-name">KTL</div>
  <div class="brand-sub">Kestrel Total Lifecare LLC</div>
  <p>Lorem Ipsum is simply dummy text of the printing and typesetting industry. Lorem Ipsum has been the industry's</p>
</div>
<div class="abs f-rule"></div>
<div class="abs copyright">© KTL KESTREL TOTAL LIFECARE LLC - 2018. All Rights Reserved.</div>
<div class="abs f-social"><span>f</span><span>t</span><span>in</span></div>

</body>
</html>
```